COOL FUN HIP PPE AD NEEDED FOR MAGAZINE

I'm looking for a fun progressive ad for a Hawaii based business magazine. Create a design that will appeal to a business that's in need of PPE to open safely. Use the Logo provided for BreezeGuard.net. These supplies are critical now for businesses to protect their clients and staff. Produce an ad that's professional, sophisticated, progressive, and to the point.

Target Market(s)

The business community who needs personal protective equipment supplies to open up their businesses safely.

Requirements
Must have
• Full page with bleed
Width 8.25 inches x Height 11.125 inches

PRINT AD FORMATS
 Adobe Illustrator® CC 2014 or earlier, Adobe Photoshop® CC 2014, Adobe InDesign® CC 2014 or earlier.

 4-color CMYK Any layouts containing RGB, Spot or Pantone colors must be converted to their CMYK equivalents. Any layouts found to have a differing color scheme must be revised accordingly. We want to ensure that colors are represented properly, therefore, the client will be notified if there are any inconsistencies in color scheme.

 All screen and printer fonts and all CMYK graphics files included. For InDesign® files, please include PDF X-1a (2001) format with files and turn bleeds on when exporting to PDF if submitting ad with bleeds.

 Offset all crop marks by 0.125".

 EPS and TIFF files: 300dpi resolution with CMYK color or grayscale at actual size with all fonts converted to outlines Press-Ready PDF files are acceptable if all fonts are embedded and images are converted to CMYK at 300 dpi. All PDFs built incorrectly will be sent back to the client for revisions. We are also obligated to alert the client if any graphic elements are under 300 dpi to ensure that advertisements are displayed at their best quality.

```html
<!DOCTYPE html>
<html lang="en">
<head>
<meta charset="utf-8">
<title>BreezeGuard.net – Personal Protection Equipment</title>
<link rel="stylesheet" href="https://fonts.googleapis.com/css2?family=Baloo+2:wght@800&family=EB+Garamond:wght@400;600;700&family=Montserrat:wght@700&display=swap">
<style>
  :root {
    --mint: #bdfcdc;
    --green: #35b27a;
    --green-dark: #2a9a66;
    --lime: #2ec52e;
    --grey: #555b5b;
    --white: #ffffff;
    --ink: #0f3d3a;
    --mask-tone: #e6f1ef;
    --bottle-tone: #bfe7f0;
    --glove-tone: #56cdf0;
    --shield-tone: #8fd3b5;
  }
  * { margin: 0; padding: 0; box-sizing: border-box; }
  html, body { width: 897px; height: 1200px; overflow: hidden; background: var(--white); }
  .ad {
    position: relative; width: 897px; height: 1200px; overflow: hidden;
    font-family: "EB Garamond", Georgia, serif; color: var(--white);
  }
  .ad__backdrop { position: absolute; left: 0; top: 0; }
  .brand {
    position: absolute; left: 54px; top: 150px;
    display: flex; align-items: center; gap: 12px;
    font-family: "EB Garamond", Georgia, serif; font-weight: 700;
    font-size: 50px; color: var(--grey); letter-spacing: -0.5px;
  }
  .brand__dot { width: 22px; height: 22px; border-radius: 50%; background: var(--lime); }
  .order-badge { position: absolute; left: 658px; top: 28px; }
  .order-badge text { font-family: "Montserrat", Arial, sans-serif; font-weight: 700; font-size: 31px; fill: var(--white); }
  .tagline {
    position: absolute; left: 475px; top: 322px; width: 370px;
    font-size: 29px; font-weight: 600; text-align: center; white-space: nowrap;
  }
  .headline {
    position: absolute; left: 460px; top: 378px; width: 390px; text-align: center;
    font-family: "Baloo 2", "Arial Black", sans-serif; font-weight: 800;
    font-size: 37px; line-height: 56px; color: var(--white); letter-spacing: 1px;
    -webkit-text-stroke: 1.5px var(--ink); paint-order: stroke fill;
    text-shadow: 1px 1px 0 var(--ink);
  }
  .products__title {
    position: absolute; left: 49px; top: 516px;
    font-size: 36px; font-weight: 700;
  }
  .product {
    position: absolute; top: 612px; width: 170px; margin-left: -85px;
    display: flex; flex-direction: column; align-items: center;
  }
  .product__art { height: 132px; border-radius: 14px; }
  .product__art--mask { width: 120px; height: 90px; margin-top: 22px; margin-bottom: 20px; border-radius: 50% 50% 45% 45%; background: var(--mask-tone); }
  .product__art--sanitizer { width: 54px; background: linear-gradient(#e8f4f4, #38d6b6); }
  .product__art--shield { width: 82px; height: 100px; margin-top: 16px; margin-bottom: 16px; background: var(--shield-tone); border-radius: 8px 8px 20px 20px; }
  .product__art--disinfectant { width: 52px; background: linear-gradient(var(--white), var(--bottle-tone)); }
  .product__art--gloves { width: 112px; height: 104px; margin-top: 14px; margin-bottom: 14px; background: var(--glove-tone); border-radius: 40% 40% 30% 30%; }
  .product__label { margin-top: 14px; font-size: 19px; font-weight: 700; white-space: nowrap; }
  .benefit {
    position: absolute; display: flex; align-items: center; gap: 44px;
    font-size: 28px; font-weight: 400; white-space: nowrap;
  }
  .benefit svg { flex: none; }
  .slogan {
    position: absolute; left: 183px; top: 1034px; width: 554px; height: 84px;
    background: var(--white); color: var(--lime);
    display: flex; align-items: center; justify-content: center;
    font-size: 36px; font-weight: 400;
  }
</style>
</head>
<body>
<main class="ad">
  <svg class="ad__backdrop" width="897" height="1200" viewBox="0 0 897 1200" aria-hidden="true">
    <rect x="13" y="13" width="871" height="1174" fill="var(--mint)"/>
    <path d="M13,439 C70,468 160,485 250,450 C370,405 420,300 520,262 C600,232 660,222 710,224 C780,226 840,236 884,248 L884,1187 L13,1187 Z" fill="var(--green)"/>
  </svg>

  <div class="brand"><span class="brand__dot"></span>BreezeGuard.net</div>

  <svg class="order-badge" width="166" height="182" viewBox="0 0 166 182" aria-label="Order Now">
    <polygon points="83,2 162,46 162,136 83,180 4,136 4,46" fill="var(--green)" stroke="var(--green)" stroke-width="4" stroke-linejoin="round"/>
    <polygon points="83,14 151,52 151,130 83,168 15,130 15,52" fill="none" stroke="var(--mint)" stroke-width="4" stroke-linejoin="round"/>
    <text x="83" y="83" text-anchor="middle">Order</text>
    <text x="83" y="123" text-anchor="middle">Now</text>
  </svg>

  <p class="tagline">Protect Yourself and Family</p>
  <h1 class="headline">Personal Protection<br>Equipment</h1>

  <h2 class="products__title">Our Products</h2>
  <div class="product" style="left:82px"><div class="product__art product__art--mask" role="img" aria-label="Illustration of a face mask"></div><span class="product__label">Face Mask</span></div>
  <div class="product" style="left:262px"><div class="product__art product__art--sanitizer" role="img" aria-label="Illustration of a hand sanitizer pump bottle"></div><span class="product__label">Hand Senitizer</span></div>
  <div class="product" style="left:448px"><div class="product__art product__art--shield" role="img" aria-label="Illustration of a clear face shield"></div><span class="product__label">Face Shield</span></div>
  <div class="product" style="left:635px"><div class="product__art product__art--disinfectant" role="img" aria-label="Illustration of a disinfectant bottle"></div><span class="product__label">Disinfectants</span></div>
  <div class="product" style="left:822px"><div class="product__art product__art--gloves" role="img" aria-label="Illustration of blue protective gloves"></div><span class="product__label">Gloves</span></div>

  <div class="benefit" style="left:50px;top:874px">
    <svg width="36" height="36" viewBox="0 0 36 36" aria-hidden="true"><circle cx="18" cy="18" r="18" fill="var(--white)"/><path d="M10,18 L16,24 L26,12" fill="none" stroke="var(--green)" stroke-width="3" stroke-linecap="round" stroke-linejoin="round"/></svg>
    Hawaii Based</div>
  <div class="benefit" style="left:50px;top:938px">
    <svg width="36" height="36" viewBox="0 0 36 36" aria-hidden="true"><circle cx="18" cy="18" r="18" fill="var(--white)"/><path d="M10,18 L16,24 L26,12" fill="none" stroke="var(--green)" stroke-width="3" stroke-linecap="round" stroke-linejoin="round"/></svg>
    Free Shipping in Hawaii</div>
  <div class="benefit" style="left:523px;top:877px">
    <svg width="36" height="36" viewBox="0 0 36 36" aria-hidden="true"><circle cx="18" cy="18" r="18" fill="var(--white)"/><path d="M10,18 L16,24 L26,12" fill="none" stroke="var(--green)" stroke-width="3" stroke-linecap="round" stroke-linejoin="round"/></svg>
    Pickup and Delivery</div>
  <div class="benefit" style="left:523px;top:936px">
    <svg width="36" height="36" viewBox="0 0 36 36" aria-hidden="true"><circle cx="18" cy="18" r="18" fill="var(--white)"/><path d="M10,18 L16,24 L26,12" fill="none" stroke="var(--green)" stroke-width="3" stroke-linecap="round" stroke-linejoin="round"/></svg>
    Quality Products</div>

  <p class="slogan">For the people of Hawaii</p>
</main>
</body>
</html>
```